Real Estate Business Cards

Looking for a clean, sharp and professional look for our Real Estate investment Fund that invests in Multi Family Apartment buildings.

Target Market(s)

Real Estate Fund

Industry/Entity Type

Real Estate

Contact Information for Business Card

Company Description: Real Estate Investment Fund
Company Name: RKW Holdings
Name: Marcus Olvane
Cell: (917) 482-0657
Email: marcus@rkwholdings-example.com
Website: www.rkwholdings-example.com
Address: 418, 9th Street, Brooklyn NY 11218

Colors

Designer to choose colors to be used in the design.

Requirements
Nice to have
• Colors to match logo

```html
<!DOCTYPE html>
<html lang="en">
<head>
<meta charset="utf-8">
<title>RKW Holdings – Business Cards</title>
<link rel="stylesheet" href="https://fonts.googleapis.com/css2?family=Cormorant+Garamond:wght@500;600&family=Quicksand:wght@400;500&display=swap">
<style>
  :root {
    --backdrop: #d8dadf;
    --card-white: #ffffff;
    --brand-blue: #1a78b8;
    --brand-blue-deep: #11609a;
    --ink-gray: #4a4c50;
    --strip-gray: #3b3c3f;
    --card-dark: #3c3d40;
    --on-dark: #ffffff;
  }
  * { margin: 0; padding: 0; box-sizing: border-box; }
  html, body {
    width: 1200px; height: 900px; overflow: hidden;
    background: var(--backdrop);
  }
  .sheet {
    position: relative; width: 1200px; height: 900px;
    display: flex; align-items: center; justify-content: center; gap: 40px;
  }
  .card {
    position: relative; width: 540px; height: 309px;
    border-radius: 4px; overflow: hidden;
    box-shadow: 0 10px 28px rgba(0,0,0,.22);
  }
  .card-front { background: var(--card-white); }
  .card-back {
    background: var(--card-dark);
    display: flex; align-items: center; justify-content: center; gap: 14px;
  }
  .front-art { position: absolute; inset: 0; }
  .brand {
    font-family: "Cormorant Garamond", serif; font-weight: 600;
    letter-spacing: 1px; text-transform: uppercase;
  }
  .card-front .brand {
    position: absolute; left: 34px; top: 26px;
    font-size: 34px; color: var(--brand-blue);
  }
  .card-back .brand { font-size: 26px; color: var(--on-dark); }
  .brand-square {
    width: 34px; height: 34px; background: var(--brand-blue);
  }
  .person { position: absolute; left: 36px; top: 82px; }
  .person-name {
    font-family: "Cormorant Garamond", serif; font-weight: 600;
    font-size: 20px; color: var(--brand-blue); letter-spacing: .5px;
    text-transform: uppercase;
  }
  .person-title {
    font-family: "Quicksand", sans-serif; font-size: 13px; color: var(--ink-gray);
    margin-top: -2px;
  }
  .contacts {
    position: absolute; left: 36px; top: 140px; list-style: none;
    font-family: "Quicksand", sans-serif; font-size: 13px; color: var(--ink-gray);
  }
  .contacts li { display: flex; align-items: center; gap: 7px; line-height: 20px; }
  .contacts svg { width: 12px; height: 12px; flex: none; }
  .address {
    position: absolute; left: 36px; top: 214px;
    font-family: "Quicksand", sans-serif; font-size: 13px; color: var(--ink-gray);
  }
</style>
</head>
<body>
<main class="sheet">
  <section class="card card-front" aria-label="Business card front">
    <svg class="front-art" viewBox="0 0 540 309" aria-hidden="true">
      <defs>
        <linearGradient id="blueFade" x1="0" y1="0" x2="0" y2="1">
          <stop offset="0" stop-color="var(--brand-blue)"/>
          <stop offset="1" stop-color="var(--brand-blue-deep)"/>
        </linearGradient>
      </defs>
      <path class="accent-panel" d="M290 309 L348 168 Q364 130 406 127 L540 116 L540 309 Z" fill="url(#blueFade)"/>
      <rect class="accent-strip" x="446" y="100" width="94" height="7" fill="var(--strip-gray)"/>
      <path class="accent-strip" d="M262 309 L296 228 L303 231 L272 309 Z" fill="var(--strip-gray)"/>
      <rect class="accent-square" x="398" y="172" width="92" height="92" fill="none" stroke="#ffffff" stroke-width="8"/>
    </svg>

    <div class="brand">RKW Holdings</div>

    <div class="person">
      <div class="person-name">Marcus Olvane</div>
      <div class="person-title">President</div>
    </div>

    <ul class="contacts">
      <li>
        <svg viewBox="0 0 12 12"><circle cx="6" cy="6" r="5.3" fill="none" stroke="var(--brand-blue)" stroke-width="1.2"/><path d="M4 3.2 L5 3 L5.6 4.6 L5 5.1 Q5.6 6.5 6.9 7 L7.4 6.4 L9 7 L8.8 8 Q6 8.6 3.8 5.2 Z" fill="var(--brand-blue)"/></svg>
        (917) 482-0657
      </li>
      <li>
        <svg viewBox="0 0 12 12"><rect x="1" y="2.5" width="10" height="7" fill="none" stroke="var(--brand-blue)" stroke-width="1.2"/><path d="M1 2.5 L6 6.5 L11 2.5" fill="none" stroke="var(--brand-blue)" stroke-width="1.2"/></svg>
        marcus@rkwholdings-example.com
      </li>
      <li>
        <svg viewBox="0 0 12 12"><circle cx="6" cy="6" r="5.2" fill="var(--brand-blue)"/><path d="M1 6 H11 M6 1 V11 M6 1 Q2.8 6 6 11 M6 1 Q9.2 6 6 11" fill="none" stroke="#fff" stroke-width=".8"/></svg>
        www.rkwholdings-example.com
      </li>
    </ul>

    <div class="address">418, 9th Street, Brooklyn NY 11218</div>
  </section>

  <section class="card card-back" aria-label="Business card back">
    <div class="brand-square"></div>
    <div class="brand">RKW Holdings</div>
  </section>
</main>
</body>
</html>
```